GVA Invitiation

We need an invitation design for a Pantry Weekly industry conference. The invitation will solicit our company's top vendors and clients who are industry ingredient manufacturers and solution providers for Consumer Packaged Goods companies. We would like to see designs that feel like an exclusive invitation to an intimate event (250 attendees) with industry thought leaders.

Target: Our company's Pantry Weekly vendors
Medium: Print invitation on standard buckslip 8.5 x 5.5. Prefer vertical orientation.
Timing: Design mechanicals delivered by December 29th
Objective: Demonstrate value of event sponsorship via exclusive invitation
Strategy: Incent vendor sponsorship via high touch sales
Considerations: existing logo, colors, paper quality suggestions, standard buck slip size; clean, modern design, corporate. Design should communicate fresh, new, modern.
Components: Invitation will be part of a mailer that includes a letter (8.5 x 10) and a no. 10 envelope. These components are NOT part of the invitation design project for Sketchtrove.

Added size of buckslip. Also added preference for vertical design as long as the text doesn't appear too crowded in that orientation.

Buckslip should be 8.5 x 5.5

Thank you all for your submissions. We are evaluating which design to choose and will be in touch shortly.

Target Market(s)

Target audience are typically food industry ingredient vendors. Adult, aged 45-50, male.

Industry/Entity Type

Industry

Font styles to use
Serif

Colors
9bcb3b

Requirements
Must have
• The Grain Vanguard Assembly logo is the main logo. Pantry Weekly logo and Corvell Media logo are secondary.

The attached word document has the copy that needs to be laid out in the invitation.
Nice to have
• Vertical orientation but not if the text is too crowded

```html
<!DOCTYPE html>
<html lang="en">
<head>
<meta charset="utf-8">
<title>Grain Vanguard Assembly 2015 – Exhibitor Invitation</title>
<link rel="stylesheet" href="https://fonts.googleapis.com/css2?family=Roboto:wght@300;400;700&family=Roboto+Condensed:wght@700&family=Quicksand:wght@500;700&display=swap">
<style>
  :root {
    --backdrop: #e9e7e3;
    --lime: #9bcb3b;
    --lime-light: #b4dc55;
    --lime-deep: #86b82c;
    --ink: #1d1f18;
    --ink-soft: #2b3a12;
    --glow: rgba(255, 255, 255, 0.92);
    --partner: #6b1f2e;
    --divider: rgba(29, 31, 24, 0.45);
  }
  * { box-sizing: border-box; margin: 0; padding: 0; }
  html, body {
    width: 1200px; height: 873px; overflow: hidden;
    background: var(--backdrop);
  }
  .sheet {
    position: relative; width: 1200px; height: 873px;
    display: flex; justify-content: center; align-items: center; gap: 44px;
  }
  .buckslip {
    width: 380px; height: 590px; position: relative;
    background:
      repeating-linear-gradient(115deg, rgba(255,255,255,0.05) 0 2px, transparent 2px 6px),
      linear-gradient(160deg, var(--lime-light) 0%, var(--lime) 45%, var(--lime-deep) 100%);
    box-shadow: 0 6px 18px rgba(0,0,0,0.18);
    color: var(--ink);
  }

  /* Front */
  .front { text-align: center; font-family: "Roboto", Arial, sans-serif; }
  .event-mark {
    position: absolute; top: 28px; left: 0; right: 0; height: 130px;
    display: flex; align-items: center; justify-content: center;
    background: radial-gradient(ellipse 62% 55% at 50% 50%, var(--glow) 0%, rgba(255,255,255,0.55) 45%, transparent 78%);
  }
  .event-mark__name {
    font-family: "Roboto Condensed", "Arial Narrow", sans-serif; font-weight: 700;
    font-size: 31px; line-height: 0.95; letter-spacing: -0.5px;
    color: var(--ink); text-transform: uppercase; text-align: left;
  }
  .event-mark__dot {
    width: 16px; height: 16px; border-radius: 50%;
    background: var(--lime-deep); margin-right: 10px; flex: none;
  }
  .invite-lead { position: absolute; top: 188px; left: 0; right: 0; }
  .invite-lead__kicker { font-weight: 300; font-size: 20px; }
  .invite-lead__title { font-weight: 700; font-size: 20px; margin-top: 2px; }
  .invite-lead__dates { font-weight: 300; font-size: 29px; margin-top: 10px; }
  .invite-lead__place { font-weight: 300; font-size: 17px; margin-top: 14px; }
  .invite-lead__web { font-weight: 400; font-size: 16px; margin-top: 2px; }
  .invite-letter {
    position: absolute; top: 370px; left: 34px; right: 34px;
    font-weight: 400; font-size: 13px; line-height: 1.45;
  }
  .partners {
    position: absolute; bottom: 30px; left: 0; right: 0;
    display: flex; justify-content: center; align-items: center; gap: 16px;
    font-family: "Roboto", Arial, sans-serif; font-size: 14px; font-weight: 700;
  }
  .partners__pantry { color: var(--partner); }
  .partners__rule { width: 1px; height: 28px; background: var(--divider); }
  .partners__corvell { color: var(--ink-soft); }

  /* Back */
  .back {
    font-family: "Quicksand", "Trebuchet MS", sans-serif;
    padding: 70px 40px 0 44px;
  }
  .back__section { margin-bottom: 26px; }
  .back__heading { font-size: 13px; font-weight: 700; letter-spacing: 0.3px; }
  .back__copy { font-size: 12.5px; font-weight: 500; line-height: 1.5; margin-top: 2px; }
</style>
</head>
<body>
<main class="sheet">

  <section class="buckslip front" aria-label="Invitation front">
    <div class="event-mark">
      <span class="event-mark__dot"></span>
      <span class="event-mark__name">The Grain Vanguard<br>Assembly 2015</span>
    </div>

    <div class="invite-lead">
      <p class="invite-lead__kicker">An Exclusive Invitation to Exhibit</p>
      <p class="invite-lead__title">The Grain Vanguard Assembly</p>
      <p class="invite-lead__dates">April 27-29, 2015</p>
      <p class="invite-lead__place">Chicago, IL</p>
      <p class="invite-lead__web">www.grainvanguardassembly.com</p>
    </div>

    <p class="invite-letter">As a valued partner, I'd like to share with you an exclusive opportunity in 2015. The Grain Vanguard Assembly, taking place in April, is the newest way to get your brand into the hands of the food and beverage professionals who will grow your business. Here is why I think you'd benefit:</p>

    <div class="partners">
      <span class="partners__pantry">Pantry Weekly</span>
      <span class="partners__rule"></span>
      <span class="partners__corvell">Corvell Media</span>
    </div>
  </section>

  <section class="buckslip back" aria-label="Invitation back">
    <div class="back__section">
      <h2 class="back__heading">THE AUDIENCE:</h2>
      <p class="back__copy">Sponsored by Pantry Weekly magazine, The Grain Vanguard Assembly will allow you to connect to 250 of the most influential decision-makers representing all aspects of the food industry. There's no other event with the content, networking opportunities and exclusive attendee list.</p>
    </div>
    <div class="back__section">
      <h2 class="back__heading">THE EVENT:</h2>
      <p class="back__copy">Designed to be small, yet effective. The Grain Vanguard Assembly ensures that your time is focused and productive with just the right people. Share your story, demo your products and technologies, develop a face-to-face relationship with your potential clients and introduce your brand to the decision-makers of today, and the thought leaders of tomorrow.</p>
    </div>
    <div class="back__section">
      <h2 class="back__heading">THE OPPORTUNITY:</h2>
      <p class="back__copy">Limited to just 25 event exhibitors, the benefit to sponsoring is the exclusivity. From turn-key exhibit opportunities to completely customizable marketing campaigns, The Grain Vanguard Assembly offers access to a unique buying audience in an array of ways. Your opportunity to gain sales leads has never been easier.</p>
    </div>
  </section>

</main>
</body>
</html>
```